automotive repair and collision repair shop card

our company is called K.R Motor service we are a automotive repair company
we also do government inspections. the company information is on the cards. I would like you to use my new logo and create a new card and use the information from my old card. Good Luck!!

Industry/Entity Type

Car Repair

Contact Information for Business Card

Address: #417-15862 91 Ave, Surrey, BC V5T 8K4
Phone:(604) 555-0187
fax 604 555 0142
website www.krmotor.example

Font styles to use
Serif
Sans Serif

Requirements
Must have
• all the information
Should not have
• the owner and there name

```html
<!DOCTYPE html>
<html lang="en">
<head>
<meta charset="utf-8">
<title>K.R Motor service – Business Card</title>
<link rel="stylesheet" href="https://fonts.googleapis.com/css2?family=PT+Sans:ital,wght@0,400;0,700;1,400&display=swap">
<style>
  :root {
    --stage: #2b2c30;
    --card-white: #ffffff;
    --card-grey: #a5a8ac;
    --charcoal: #333436;
    --ink: #1d1d1f;
    --faint-ring: #ececec;
    --silver: #d9dadc;
    --text-light: #f2f2f2;
  }
  * { box-sizing: border-box; margin: 0; padding: 0; }
  html, body { width: 1200px; height: 900px; overflow: hidden; }
  body {
    background: var(--stage);
    font-family: "PT Sans", Arial, sans-serif;
    display: flex;
    align-items: center;
    justify-content: center;
    gap: 40px;
  }
  .card {
    position: relative;
    width: 520px;
    height: 297px;
    overflow: hidden;
    box-shadow: 0 12px 30px rgba(0,0,0,.45);
  }
  /* Front */
  .card--front { background: var(--card-white); }
  .front__ring {
    position: absolute;
    left: 50%; top: 50%;
    width: 210px; height: 210px;
    margin: -105px 0 0 -105px;
    border-radius: 50%;
    background: var(--faint-ring);
  }
  .brand {
    position: absolute;
    left: 0; right: 0; top: 50%;
    transform: translateY(-50%);
    text-align: center;
    color: var(--ink);
  }
  .brand__name {
    font-size: 44px;
    font-weight: 400;
    letter-spacing: 1px;
    text-transform: uppercase;
    line-height: 1;
  }
  .brand__tagline {
    margin-top: 8px;
    font-size: 17px;
    font-style: italic;
  }
  /* Back */
  .card--back { background: var(--card-grey); }
  .back__shapes { position: absolute; inset: 0; }
  .back__brand {
    position: absolute;
    left: 22px; top: 112px;
    color: var(--ink);
  }
  .back__brand .brand__name { font-size: 26px; }
  .back__brand .brand__tagline { font-size: 11px; margin-top: 4px; }
  .contact {
    position: absolute;
    right: 18px; top: 36px;
    list-style: none;
    color: var(--text-light);
    font-size: 12.5px;
    text-align: right;
  }
  .contact li {
    display: flex;
    align-items: center;
    justify-content: flex-end;
    gap: 8px;
    height: 21px;
  }
  .contact svg { width: 13px; height: 13px; flex: none; }
  .address {
    position: absolute;
    right: 18px; top: 238px;
    font-size: 12.5px;
    color: var(--ink);
  }
</style>
</head>
<body>

  <section class="card card--front" aria-label="Business card front">
    <div class="front__ring"></div>
    <div class="brand">
      <p class="brand__name">K.R Motor service</p>
      <p class="brand__tagline">One Stop Repair Shop</p>
    </div>
  </section>

  <section class="card card--back" aria-label="Business card back">
    <svg class="back__shapes" viewBox="0 0 520 297" aria-hidden="true">
      <defs>
        <linearGradient id="band" x1="0" x2="1" y1="0" y2="0">
          <stop offset="0" stop-color="#3a3b3d"/>
          <stop offset="0.45" stop-color="#bfc0c2"/>
          <stop offset="1" stop-color="#ffffff"/>
        </linearGradient>
      </defs>
      <path d="M150 297 Q 215 105 430 42 L520 28 L520 297 Z" fill="var(--charcoal)"/>
      <path d="M150 297 Q 215 105 430 42 L520 28" fill="none" stroke="var(--silver)" stroke-width="3" opacity=".7"/>
      <rect x="150" y="230" width="370" height="34" fill="url(#band)"/>
      <rect x="150" y="264" width="370" height="33" fill="#111112"/>
    </svg>

    <div class="back__brand">
      <p class="brand__name">K.R Motor service</p>
      <p class="brand__tagline">One Stop Repair Shop</p>
    </div>

    <ul class="contact">
      <li>604 555 0142
        <svg viewBox="0 0 16 16"><rect x="2" y="6" width="12" height="7" rx="1" fill="currentColor"/><rect x="4" y="2" width="8" height="4" fill="currentColor"/></svg>
      </li>
      <li>(604) 555-0187
        <svg viewBox="0 0 16 16"><path d="M4 1.5l2.5 3-1.5 1.5a8 8 0 0 0 5 5l1.5-1.5 3 2.5-1.5 2.5C7 14 2 9 1.5 3z" fill="currentColor"/></svg>
      </li>
      <li>info@krmotor.example
        <svg viewBox="0 0 16 16"><rect x="1.5" y="3.5" width="13" height="9" fill="none" stroke="currentColor"/><path d="M1.5 3.5L8 9l6.5-5.5" fill="none" stroke="currentColor"/></svg>
      </li>
      <li>www.krmotor.example
        <svg viewBox="0 0 16 16"><circle cx="8" cy="8" r="6.5" fill="none" stroke="currentColor"/><ellipse cx="8" cy="8" rx="3" ry="6.5" fill="none" stroke="currentColor"/><path d="M1.5 8h13" stroke="currentColor"/></svg>
      </li>
    </ul>

    <p class="address">#417-15862 91 Ave, Surrey, BC V5T 8K4</p>
  </section>

</body>
</html>
```